Soccer Training for Boys and Girls

I need like a flyer to post on facebook and instagram.
This is what O want to have on it.
you can use any color , soccer field on the background , or any soccer pictures.
Recreational and Travel Teams
Ages :5 to 14 years old
Field: Hollis Vantree Middle School (3478 Pelican dr Silver spring, MD 20817)
Register online www.dunmarelacademy.example
-passing
-kicking
-shooting
-dribbling
-ball Control
Registration :$210 (includes 1st month, registration, practice Uniform
after 1st month.

Call us Phone:(240)555-0187

• kids playing soccer , soccer fields

```html
<!DOCTYPE html>
<html lang="en">
<head>
<meta charset="utf-8">
<title>Dunmarel Soccer Academy – Training Flyer</title>
<link rel="stylesheet" href="https://fonts.googleapis.com/css2?family=Exo+2:ital,wght@1,800;1,900&family=Montserrat:wght@500;600;700&display=swap">
<style>
  :root {
    --stage: #4a4a4c;
    --white: #ffffff;
    --paper: #f1f1f1;
    --ink: #111111;
    --night: #1f1f20;
    --night-soft: #2b2b2d;
    --royal: #1b5aa6;
    --royal-deep: #12447f;
    --sky: #4a90d9;
    --grass: #6f8f4e;
    --foliage: #3f5a2c;
  }
  html, body {
    margin: 0;
    width: 1200px;
    height: 1000px;
    overflow: hidden;
    background: var(--stage);
  }
  .flyer {
    position: absolute;
    left: 157px;
    top: 57px;
    width: 888px;
    height: 888px;
    overflow: hidden;
    background: var(--night);
    box-shadow: 0 6px 18px rgba(0,0,0,.45);
    font-family: "Montserrat", Arial, sans-serif;
  }
  .flyer-shapes { position: absolute; inset: 0; }
  .brand {
    position: absolute;
    left: 78px;
    top: 88px;
    display: flex;
    align-items: center;
    gap: 16px;
  }
  .brand-mark {
    width: 78px; height: 78px;
    border-radius: 50%;
    background: var(--royal);
    flex: none;
  }
  .brand-name {
    font-family: "Exo 2", sans-serif;
    font-style: italic;
    font-weight: 900;
    font-size: 30px;
    line-height: 1.05;
    color: var(--royal);
    text-transform: uppercase;
  }
  .venue {
    position: absolute;
    left: 68px;
    top: 318px;
    margin: 0;
    font-family: "Exo 2", sans-serif;
    font-style: italic;
    font-weight: 900;
    text-transform: uppercase;
    line-height: 1;
  }
  .venue-accent { display: block; color: var(--sky); font-size: 68px; letter-spacing: 1px; }
  .venue-mid { display: block; color: var(--white); font-size: 40px; margin: 6px 0 4px; }
  .address {
    position: absolute;
    left: 62px;
    top: 528px;
    margin: 0;
    font-weight: 700;
    font-size: 28px;
    line-height: 40px;
    color: var(--ink);
  }
  .skills {
    position: absolute;
    left: 60px;
    top: 662px;
    margin: 0; padding: 0;
    list-style: none;
  }
  .skill {
    display: flex;
    align-items: center;
    gap: 32px;
    height: 41.5px;
    color: var(--white);
    font-weight: 500;
    font-size: 30px;
  }
  .skill svg { width: 34px; height: 34px; flex: none; }
  .register-label {
    position: absolute;
    left: 575px; width: 200px;
    top: 400px;
    margin: 0;
    text-align: center;
    color: var(--white);
    font-weight: 700;
    font-size: 28px;
    line-height: 40px;
  }
  .web {
    position: absolute;
    right: 60px;
    top: 498px;
    margin: 0;
    color: var(--white);
    font-weight: 600;
    font-size: 26px;
  }
  .pricing {
    position: absolute;
    right: 56px;
    top: 566px;
    margin: 0;
    text-align: right;
    color: var(--white);
  }
  .price { display: block; font-weight: 500; font-size: 39px; line-height: 52px; }
  .price-note { display: block; font-weight: 500; font-size: 23px; line-height: 32px; }
  .price-after { display: block; font-weight: 500; font-size: 38px; line-height: 58px; }
  .call {
    position: absolute;
    right: 56px;
    top: 758px;
    margin: 0;
    color: var(--white);
    font-weight: 700;
    font-size: 33px;
  }
  .phone {
    position: absolute;
    right: 56px;
    top: 820px;
    margin: 0;
    display: flex;
    align-items: center;
    gap: 14px;
    color: var(--white);
    font-weight: 700;
    font-size: 34px;
  }
  .phone svg { width: 30px; height: 30px; }
</style>
</head>
<body>
<main class="flyer">
  <svg class="flyer-shapes" viewBox="0 0 888 888" width="888" height="888" aria-hidden="false">
    <defs>
      <linearGradient id="fieldTone" x1="0" y1="0" x2="0" y2="1">
        <stop offset="0" stop-color="var(--foliage)"/>
        <stop offset=".55" stop-color="#5a7a6a"/>
        <stop offset="1" stop-color="var(--grass)"/>
      </linearGradient>
    </defs>
    <!-- light header -->
    <rect class="header-bg" x="0" y="0" width="888" height="305" fill="var(--paper)"/>
    <polygon points="0,0 300,0 120,180 0,180" fill="var(--white)" opacity=".7"/>
    <!-- dark lower area -->
    <polygon class="dark-band" points="0,305 560,305 560,888 0,888" fill="var(--night)"/>
    <polygon points="0,643 260,643 60,888 0,888" fill="var(--night-soft)"/>
    <!-- photo -->
    <polygon class="photo" role="img" aria-label="Photo of young players in blue kits running on a soccer field" points="406,0 888,0 888,430 540,430 383,183" fill="url(#fieldTone)"/>
    <polyline points="383,0 360,183 540,430" fill="none" stroke="var(--royal)" stroke-width="3"/>
    <polyline points="840,0 888,48" fill="none" stroke="var(--royal)" stroke-width="3"/>
    <!-- address band -->
    <polygon class="address-band" points="0,518 380,518 338,643 0,643" fill="var(--white)"/>
    <!-- register block -->
    <polygon points="698,288 888,478 888,490 496,490" fill="var(--royal)"/>
    <polyline points="560,490 698,352 860,490" fill="none" stroke="var(--white)" stroke-width="3"/>
    <!-- url band -->
    <polygon points="343,488 888,488 888,543 398,543" fill="var(--night)"/>
    <!-- price block -->
    <polygon points="428,543 888,543 888,755 460,755 338,633" fill="var(--royal-deep)"/>
    <polyline points="440,560 355,645 600,888" fill="none" stroke="var(--white)" stroke-width="3"/>
    <!-- call band -->
    <polygon points="470,755 888,755 888,803 518,803" fill="var(--night)"/>
    <!-- phone block -->
    <polygon points="518,803 888,803 888,888 603,888" fill="var(--royal)"/>
  </svg>

  <div class="brand">
    <span class="brand-mark"></span>
    <span class="brand-name">Dunmarel<br>Soccer Academy</span>
  </div>

  <h1 class="venue">
    <span class="venue-accent">Hollis</span>
    <span class="venue-mid">Vantree Middle</span>
    <span class="venue-accent">School</span>
  </h1>

  <p class="address">(3478 Pelican<br>dr Silver spring,<br>MD 20817)</p>

  <ul class="skills">
    <li class="skill"><svg viewBox="0 0 34 34"><circle cx="15" cy="18" r="13" fill="none" stroke="var(--sky)" stroke-width="2.5"/><polyline points="9,17 15,23 30,6" fill="none" stroke="var(--sky)" stroke-width="3"/></svg>Passing</li>
    <li class="skill"><svg viewBox="0 0 34 34"><circle cx="15" cy="18" r="13" fill="none" stroke="var(--sky)" stroke-width="2.5"/><polyline points="9,17 15,23 30,6" fill="none" stroke="var(--sky)" stroke-width="3"/></svg>Kicking</li>
    <li class="skill"><svg viewBox="0 0 34 34"><circle cx="15" cy="18" r="13" fill="none" stroke="var(--sky)" stroke-width="2.5"/><polyline points="9,17 15,23 30,6" fill="none" stroke="var(--sky)" stroke-width="3"/></svg>Shooting</li>
    <li class="skill"><svg viewBox="0 0 34 34"><circle cx="15" cy="18" r="13" fill="none" stroke="var(--sky)" stroke-width="2.5"/><polyline points="9,17 15,23 30,6" fill="none" stroke="var(--sky)" stroke-width="3"/></svg>Dribbling</li>
    <li class="skill"><svg viewBox="0 0 34 34"><circle cx="15" cy="18" r="13" fill="none" stroke="var(--sky)" stroke-width="2.5"/><polyline points="9,17 15,23 30,6" fill="none" stroke="var(--sky)" stroke-width="3"/></svg>Ball Control</li>
  </ul>

  <p class="register-label">REGISTER<br>ONLINE</p>
  <p class="web">www.dunmarelacademy.example</p>

  <p class="pricing">
    <span class="price">Registration :$210</span>
    <span class="price-note">(includes 1st month, registration,</span>
    <span class="price-note">practice Uniform</span>
    <span class="price-after">after 1st month.</span>
  </p>

  <p class="call">CALL US NOW!</p>
  <p class="phone">
    <svg viewBox="0 0 24 24"><path d="M6.6 10.8a15 15 0 0 0 6.6 6.6l2.2-2.2a1 1 0 0 1 1-.25 11.4 11.4 0 0 0 3.6.57 1 1 0 0 1 1 1V20a1 1 0 0 1-1 1A17 17 0 0 1 3 4a1 1 0 0 1 1-1h3.5a1 1 0 0 1 1 1c0 1.25.2 2.45.57 3.57a1 1 0 0 1-.25 1z" fill="var(--white)"/></svg>
    (240)555-0187
  </p>
</main>
</body>
</html>
```